Label Design for Men's Vitamin supplement "Kestravon"

Design a bottle label for a Men's Vitamin supplement "Kestravon". It is for a men's line so it should be manly. It should convey energy and vitality without using those words. See the attached sample of what we currently are using.

Industry/Entity Type

Supplement

```html
<!DOCTYPE html>
<html lang="en">
<head>
<meta charset="utf-8">
<title>Kestravon Men's Multivitamin Label</title>
<link rel="stylesheet" href="https://fonts.googleapis.com/css2?family=Exo+2:wght@700;800;900&display=swap">
<style>
  :root {
    --stage-top: #8a8a8a;
    --stage-bottom: #4a4a4a;
    --label-black: #111214;
    --label-charcoal: #2a2c30;
    --brand-white: #f2f2f2;
    --accent-dot: #c8102e;
    --banner-green-dark: #0f5a2a;
    --banner-green-light: #2f9a4c;
    --banner-edge: #7fd08c;
    --silver-light: #f4f4f4;
    --silver-dark: #a9a9a9;
    --gold-light: #e2c07a;
    --gold-dark: #a67c2c;
    --ink-dark: #1b1b1b;
  }
  * { margin: 0; padding: 0; box-sizing: border-box; }
  html, body {
    width: 1200px;
    height: 884px;
    overflow: hidden;
  }
  body {
    background: linear-gradient(180deg, var(--stage-top), var(--stage-bottom));
    font-family: "Exo 2", Arial, sans-serif;
    position: relative;
  }
  .label {
    position: absolute;
    left: 150px;
    top: 162px;
    width: 900px;
    height: 560px;
    overflow: hidden;
    background: var(--label-black);
    box-shadow: 0 14px 40px rgba(0,0,0,0.45);
  }
  .label-texture {
    position: absolute;
    inset: 0;
    background: radial-gradient(ellipse at 45% 40%, var(--label-charcoal) 0%, var(--label-black) 70%);
  }
  .brand {
    position: absolute;
    left: 80px;
    top: 96px;
    display: flex;
    align-items: center;
    gap: 22px;
  }
  .brand-dot {
    width: 30px;
    height: 30px;
    border-radius: 50%;
    background: var(--accent-dot);
  }
  .brand-name {
    font-weight: 900;
    font-size: 112px;
    line-height: 1;
    letter-spacing: 1px;
    color: var(--brand-white);
    text-transform: uppercase;
  }
  .banner {
    position: absolute;
    height: 58px;
    display: flex;
    align-items: center;
    padding-left: 52px;
    color: var(--brand-white);
    font-weight: 800;
    font-style: italic;
    font-size: 29px;
    text-transform: uppercase;
    letter-spacing: 0.5px;
    background: linear-gradient(90deg, var(--banner-green-dark), var(--banner-green-light) 55%, var(--banner-green-dark));
    border-top: 2px solid var(--banner-edge);
    clip-path: polygon(3% 0, 100% 0, 97% 100%, 0 100%);
  }
  .banner-purpose { left: 70px; top: 262px; width: 610px; }
  .banner-dose { left: 70px; top: 332px; width: 560px; }
  .info-band {
    position: absolute;
    left: 0;
    top: 425px;
    width: 900px;
    height: 62px;
    display: flex;
    align-items: center;
    justify-content: space-between;
    padding: 0 56px 0 40px;
    background: linear-gradient(180deg, var(--silver-light), var(--silver-dark));
    border-bottom: 3px solid var(--banner-green-light);
    color: var(--ink-dark);
    font-weight: 800;
  }
  .tablet-count { font-size: 36px; }
  .web-address { font-size: 24px; letter-spacing: 1px; text-transform: uppercase; }
  .supply-band {
    position: absolute;
    right: 0;
    top: 490px;
    width: 430px;
    height: 42px;
    display: flex;
    align-items: center;
    justify-content: flex-end;
    padding-right: 56px;
    background: linear-gradient(90deg, var(--gold-dark), var(--gold-light) 60%, var(--gold-dark));
    clip-path: polygon(8% 0, 100% 0, 100% 100%, 0 100%);
    color: var(--brand-white);
    font-weight: 800;
    font-size: 24px;
    text-transform: uppercase;
    letter-spacing: 1px;
  }
</style>
</head>
<body>
  <main class="label">
    <div class="label-texture" role="img" aria-label="Dark carbon hexagon texture behind the label content"></div>
    <div class="brand">
      <span class="brand-dot"></span>
      <span class="brand-name">Kestravon</span>
    </div>
    <div class="banner banner-purpose">Formulated for Men's Health</div>
    <div class="banner banner-dose">Once a Day Multi Vitamin</div>
    <div class="info-band">
      <span class="tablet-count">30 Tablets</span>
      <span class="web-address">Kestravon.com</span>
    </div>
    <div class="supply-band">30 Day Supply</div>
  </main>
</body>
</html>
```